Anzeigengestaltung für Immobilienmakler
Zielgruppe
Immobilienmakler, Zielgruppe: Private (selten gewerbliche) Immobilienverkäufer/-käufer, Immobilienvermietung
Aufgabenstellung
Unser Logo soll Berücksichtigung finden, gerne auch wir als Personen. Design angelehnt an Logo und Schriftbild (siehe Anhang) und Website.
Headline: Ihre Immobilienvermittler für die Bodenseeregion.
Vorteile darstellen:
- Lokale Marktkenntnis: Wir kennen die Besonderheiten des regionalen Immobilienmarkts
-Persönliche Betreuung: Bei uns stehen Sie im Mittelpunkt
- Starkes Netzwerk: Profitieren Sie von unseren guten Beziehungen
- Kompletter Service: Von der ersten Beratung über die Erstellung des Exposés bis hin zur Vertragsabwicklung – wir bieten Ihnen alles aus einer Hand.
- Ausgebildet: GWA zertifizierte Immobilienmakler und Verbandszugehörigkeit
Kontaktdaten angeben:Festnetz/ Mobilfunknummer und Homepage, Ort: Salem
Das ganze in einem klaren und wertigen Design.
Die Anzeige soll sich im Text anpassen lassen und bitte in verschiedenen Formaten ausgeworfen werden (verschiedene Größen, ggf. kleinere Größen mit weniger textlichem Inhalt)

```html
<!DOCTYPE html>
<html lang="de">
<head>
<meta charset="utf-8">
<title>Anzeigen – Uferheim Immobilien</title>
<link rel="stylesheet" href="https://fonts.googleapis.com/css2?family=Roboto:wght@400;500&display=swap">
<style>
  :root {
    --navy: #34496e;
    --slate: #6f84a3;
    --paper: #ffffff;
    --stage: #ffffff;
    --ink-light: #ffffff;
    --edge: #c9ced8;
  }
  * { margin: 0; padding: 0; box-sizing: border-box; }
  html, body { width: 1200px; height: 848px; overflow: hidden; background: var(--stage); }
  body { position: relative; font-family: "Roboto", Arial, sans-serif; }

  .ad { position: absolute; background: var(--paper); overflow: hidden; border: 1px solid var(--edge); }
  .ad-large { left: 105px; top: 68px; width: 518px; height: 718px; }
  .ad-small { left: 735px; top: 192px; width: 340px; height: 470px; }

  .ad-backdrop { position: absolute; left: 0; top: 0; width: 100%; }
  .ad-backdrop path { fill: var(--navy); }

  .headline {
    position: absolute; left: 0; width: 100%; text-align: center;
    color: var(--ink-light); font-weight: 500; text-transform: uppercase;
  }
  .ad-large .headline { top: 26px; font-size: 36px; line-height: 42px; }
  .ad-small .headline { top: 24px; font-size: 26px; line-height: 30.5px; }

  .benefits { position: absolute; left: 0; width: 100%; text-align: center; color: var(--ink-light); list-style: none; }
  .ad-large .benefits { top: 157px; padding: 0 30px; }
  .benefit { margin-bottom: 8px; }
  .benefit-title { display: block; font-weight: 500; font-size: 16px; line-height: 20px; }
  .benefit-text { display: block; font-size: 12.5px; line-height: 16px; font-weight: 400; }

  .ad-small .benefits { top: 134px; font-size: 16px; line-height: 22.6px; font-weight: 400; }

  .brand { position: absolute; display: flex; align-items: center; color: var(--navy); font-weight: 400; white-space: nowrap; }
  .brand-mark { flex: none; border-radius: 50%; background: var(--slate); }

  .ad-large .brand { left: 22px; top: 578px; font-size: 23px; gap: 10px; }
  .ad-large .brand-mark { width: 34px; height: 34px; }

  .ad-small .brand { left: 0; width: 100%; justify-content: center; top: 352px; font-size: 19px; gap: 8px; }
  .ad-small .brand-mark { width: 28px; height: 28px; }

  .contact { position: absolute; color: var(--navy); font-size: 11px; line-height: 15px; }
  .ad-large .contact { left: 16px; top: 654px; }
  .ad-small .contact { left: 0; width: 100%; top: 410px; text-align: center; }

  .team-photo {
    position: absolute; left: 283px; top: 455px; width: 222px; height: 237px;
    background: linear-gradient(180deg, #eef0f4 0%, #4a5468 50%, #2a3140 100%);
  }

  .address-bar {
    position: absolute; left: 0; bottom: 0; width: 100%; background: var(--navy);
    color: var(--ink-light); text-align: center; font-weight: 400;
  }
  .ad-large .address-bar { height: 27px; line-height: 27px; font-size: 13px; }
  .ad-small .address-bar { height: 24px; line-height: 24px; font-size: 12px; }
</style>
</head>
<body>

  <section class="ad ad-large">
    <svg class="ad-backdrop" viewBox="0 0 518 440" width="518" height="440" aria-hidden="true">
      <path d="M0 0 H518 V404 C466 392 416 388 357 400 C288 414 208 426 139 418 C80 411 40 400 0 404 Z"/>
    </svg>
    <h1 class="headline">Ihre Immobilien-<br>vermittler für die<br>Bodenseeregion.</h1>
    <ul class="benefits">
      <li class="benefit"><span class="benefit-title">Lokale Marktkenntnis:</span><span class="benefit-text">Wir kennen die Besonderheiten des regionalen Immobilienmarkts</span></li>
      <li class="benefit"><span class="benefit-title">Persönliche Betreuung:</span><span class="benefit-text">Bei uns stehen Sie im Mittelpunkt</span></li>
      <li class="benefit"><span class="benefit-title">Starkes Netzwerk:</span><span class="benefit-text">Profitieren Sie von unseren guten Beziehungen</span></li>
      <li class="benefit"><span class="benefit-title">Kompletter Service:</span><span class="benefit-text">Von der ersten Beratung über die Erstellung des Exposés bis hin zur Vertragsabwicklung&nbsp; wir bieten Ihnen alles aus einer Hand.</span></li>
      <li class="benefit"><span class="benefit-title">Ausgebildet:</span><span class="benefit-text">GWA zertifizierte Immobilienmakler und Verbandszugehörigkeit</span></li>
    </ul>
    <div class="brand"><span class="brand-mark"></span>Uferheim Immobilien</div>
    <div class="team-photo" role="img" aria-label="Porträtfoto des Maklerteams: eine Frau und ein Mann in Business-Kleidung"></div>
    <p class="contact">T: +49 (0)7553 000123 · M: +49 (0)151 00012345<br>E-Mail: kontakt@uferheim.de</p>
    <div class="address-bar">Am Seeblick 4/1 &nbsp;· 88690 Salem</div>
  </section>

  <section class="ad ad-small">
    <svg class="ad-backdrop" viewBox="0 0 340 280" width="340" height="280" aria-hidden="true">
      <path d="M0 0 H340 V245 C298 240 258 246 208 256 C158 266 109 270 69 262 C40 256 20 248 0 248 Z"/>
    </svg>
    <h1 class="headline">Ihre Immobilien-<br>vermittler für die<br>Bodenseeregion.</h1>
    <ul class="benefits">
      <li>- Lokale Marktkenntnis</li>
      <li>- Persönliche Betreuung</li>
      <li>- Starkes Netzwerk</li>
      <li>- Kompletter Service</li>
      <li>- Bestens Ausgebildet</li>
    </ul>
    <div class="brand"><span class="brand-mark"></span>Uferheim Immobilien</div>
    <p class="contact">T: +49 (0)7553 000123 · M: +49 (0)151 00012345<br>E-Mail: kontakt@uferheim.de</p>
    <div class="address-bar">Am Seeblick 4/1 &nbsp;· 88690 Salem</div>
  </section>

</body>
</html>
```